Lakeshore Freightways Guild Web Update

Update wordpress based association web site. Please look up www.lakeshorefreightwaysguild.com for our web site to get a feel for what we currently having. We would like our updated web site to look similar to: www.brightoakline.com. We will provide our key points for updating in a future email.

Target Market(s)

duplicate the brightoakline.com format please.

Number of Pages Required

4 page

Font styles to use
Serif

Requirements
Must have
• duplicate the brightoakline.com format please. You will keep most of the content that we currently have on our website.
Nice to have
• n/a
Should not have
• n/a

```html
<!DOCTYPE html>
<html lang="en">
<head>
<meta charset="utf-8">
<title>Lakeshore Freightways Guild</title>
<link href="https://fonts.googleapis.com/css2?family=Arimo:wght@400;700&display=swap" rel="stylesheet">
<style>
:root{
  --navy:#1b1f7a;
  --navy-deep:#12166a;
  --heading:#202a86;
  --purple:rgba(86,52,160,.86);
  --rust:rgba(176,88,52,.84);
  --sky:rgba(28,132,204,.84);
  --amber:rgba(232,134,28,.86);
  --white:#ffffff;
  --link-red:#e8332a;
  --topbar:#f2f2f2;
  --muted:#555;
  --divider:rgba(255,255,255,.25);
}
*{box-sizing:border-box;margin:0;padding:0}
html,body{width:1200px;height:4145px;overflow:hidden;background:#fff}
body{font-family:"Arimo",Arial,sans-serif;color:#222;position:relative}
.abs{position:absolute}
.topbar{left:0;top:0;width:1200px;height:20px;background:var(--topbar);font-size:8px;color:var(--muted);display:flex;align-items:center;padding:0 18px;gap:14px}
.topbar .socials{margin-left:auto;display:flex;gap:5px}
.dot{width:9px;height:9px;border-radius:50%;background:var(--navy)}
.header{left:0;top:20px;width:1200px;height:66px;background:#fff;display:flex;align-items:center;padding:0 22px}
.brand{display:flex;align-items:center;gap:10px;font-weight:700;color:var(--navy);font-size:22px;letter-spacing:.5px}
.brand .mark{width:22px;height:22px;background:var(--navy)}
.header .actions{margin-left:auto;display:flex;gap:6px}
.btn-menu{border:1px solid #999;color:#666;font-size:10px;padding:5px 10px;border-radius:3px}
.btn-login{background:var(--navy);color:#fff;font-size:10px;padding:5px 10px;border-radius:3px}
.hero{left:0;top:86px;width:1200px;height:576px;background:linear-gradient(180deg,#1c3c72 0%,#5c6f9a 40%,#c98a5a 72%,#3a2a28 100%)}
.hero-title{left:150px;top:240px;width:460px;color:#fff;font-weight:700;font-size:21px;line-height:29px}
.slider-dots{right:32px;top:620px;display:flex;gap:7px}
.slider-dots span{width:9px;height:9px;border-radius:50%;background:rgba(255,255,255,.6)}
.slider-dots span:first-child{background:#2a7de1}
.chev{left:585px;top:600px}
.section-title{left:0;width:1200px;text-align:center;color:var(--heading);font-weight:700;font-size:21px}
.photo{left:0;width:1200px}
.panel{color:#fff;font-size:13px;line-height:22px;letter-spacing:.3px;padding:44px 38px}
.inner-photo{position:absolute}
.signature{position:absolute;right:36px;bottom:40px;display:flex;align-items:center;gap:10px;text-align:right;font-weight:700;font-size:12px;line-height:16px}
.avatar{width:44px;height:44px;border-radius:50%;background:linear-gradient(135deg,#bbb,#777);border:2px solid #fff}
.red{color:var(--link-red)}
.outline-btn{display:inline-block;border:1px solid #fff;border-radius:3px;color:#fff;font-size:13px;padding:10px 18px}
.field{width:340px;height:34px;background:#fff;color:#999;font-size:12px;padding:10px 12px;margin-bottom:14px;border-radius:2px}
.contact-band{left:0;top:3880px;width:1200px;height:265px;background:var(--navy-deep)}
.contact-buttons{left:78px;top:3940px;display:flex;flex-direction:column;gap:14px}
.contact-buttons span{display:block;width:150px;text-align:center;border:1px solid #fff;color:#fff;font-size:11px;padding:9px 0;border-radius:3px}
.contact-item{color:#fff;font-weight:700;font-size:12px;line-height:17px;text-align:center}
.contact-item svg{display:block;margin:0 auto 8px}
.footbar{left:0;top:4050px;width:1200px;height:95px;border-top:1px solid var(--divider);color:#fff;font-size:11px;display:flex;align-items:flex-start;padding:18px 18px}
.footbar .socials{margin-left:auto;display:flex;gap:10px}
.footbar .socials span{width:12px;height:12px;border-radius:50%;background:#fff}
</style>
</head>
<body>

<div class="abs topbar">
  <span>410 Harbor Street, Suite 200 Muskegon, MI 49440</span>
  <span>(555) 214-0187</span>
  <span>(555) 214-0190</span>
  <span>office@lakeshorefreightwaysguild.com</span>
  <div class="socials"><span class="dot"></span><span class="dot"></span><span class="dot"></span><span class="dot"></span><span class="dot"></span></div>
</div>

<header class="abs header">
  <div class="brand"><span class="mark"></span>Lakeshore Freightways Guild</div>
  <div class="actions"><span class="btn-menu">Menu ☰</span><span class="btn-login">Login</span></div>
</header>

<section>
  <div class="abs hero" role="img" aria-label="Freight locomotive hauling cars at dusk under a blue and orange sky"></div>
  <h1 class="abs hero-title">Every year America's freight railroads spend more than $20 billion annually of their own funds, not taxpayer money, to build and maintain a rail network that is safe, reliable, efficient and affordable.</h1>
  <svg class="abs chev" width="30" height="18" viewBox="0 0 30 18"><polyline points="3,3 15,14 27,3" fill="none" stroke="#fff" stroke-width="3"/></svg>
  <div class="abs slider-dots"><span></span><span></span><span></span><span></span></div>
</section>

<h2 class="abs section-title" style="top:698px">Welcome to LFG</h2>
<section>
  <div class="abs photo" style="top:755px;height:495px;background:linear-gradient(90deg,#0c1a3a 0%,#28407a 40%,#1d2a56 75%,#14204a 100%)" role="img" aria-label="Blue and white locomotive at night"></div>
  <div class="abs panel" style="left:605px;top:755px;width:410px;height:495px;background:var(--purple)">
    I would like to welcome you to the Lakeshore Freightways Guild website. Here you will find valuable information on Michigan railroads, including issues and concerns in and around the railroad industry. We are an active and aggressive state railroad association and we look forward to continued success with our partnerships. Please make sure to click on our member railroad company links while you're here. Also, sign up for our newsletter and follow the LFG on social media. Thank you and I hope you enjoy your visit to our website.
    <div class="signature"><div>Dale Brennan<br>President</div><div class="avatar" role="img" aria-label="Portrait of the president"></div></div>
  </div>
</section>

<h2 class="abs section-title" style="top:1280px">What We DO</h2>
<section>
  <div class="abs photo" style="top:1340px;height:560px;background:linear-gradient(90deg,#3f5a2a 0%,#6b7a3e 45%,#c98a2a 65%,#4a5f30 100%)" role="img" aria-label="Orange locomotive among green trees"></div>
  <div class="abs panel" style="left:170px;top:1340px;width:420px;height:560px;background:var(--rust)">
    The LFG reviews all introduced legislation in the House and Senate. Proposed legislation affecting the rail industry is shared with our members. Final industry positions regarding legislation are then communicated to the legislature. We pursue the same activity with appropriate personnel in the state departments and the legislative rules process.
    <div class="inner-photo" style="left:55px;top:295px;width:320px;height:195px;background:linear-gradient(180deg,#9fbcd8 0%,#b8c4b0 55%,#6e7450 100%)" role="img" aria-label="Red locomotives on a track"></div>
  </div>
</section>

<h2 class="abs section-title" style="top:1960px">Who We Are</h2>
<section>
  <div class="abs photo" style="top:2020px;height:560px;background:linear-gradient(90deg,#3b6fa0 0%,#a8c4dc 40%,#d8e4ee 60%,#4a7aa6 100%)" role="img" aria-label="Red locomotive plowing through snow"></div>
  <div class="abs panel" style="left:605px;top:2020px;width:420px;height:560px;background:var(--sky)">
    The Lakeshore Freightways Guild (LFG) is a non-profit trade association that represents the interests of freight railroads operating in Michigan. LFG members range in size from large Class 1 interstate carriers to smaller regional carriers and shortline railroads. LFG members account for over 95% of all freight rail moved in Michigan.
    <div class="inner-photo" style="left:45px;top:285px;width:320px;height:215px;background:linear-gradient(180deg,#8fb070 0%,#5e8040 55%,#6b6050 100%)" role="img" aria-label="Video still of a freight train through green countryside"></div>
    <svg class="inner-photo" style="left:188px;top:375px" width="34" height="26" viewBox="0 0 34 26"><rect width="34" height="26" rx="5" fill="#fff"/><polygon points="13,7 23,13 13,19" fill="#222"/></svg>
  </div>
</section>

<h2 class="abs section-title" style="top:2640px">How to Join LFG</h2>
<section>
  <div class="abs photo" style="top:2700px;height:555px;background:linear-gradient(90deg,#4f6a30 0%,#7a8a50 40%,#9fb8d4 60%,#3e5a30 100%)" role="img" aria-label="Freight train with containers passing a lakeshore town"></div>
  <div class="abs panel" style="left:170px;top:2700px;width:420px;height:555px;background:var(--amber)">
    LFG membership is open to any freight railroad with Michigan operations. Please contact the LFG office for membership information. Companies which supply goods or services to the railroad industry are eligible for a non-voting Associate Membership. Annual dues are $1,000 per year for supplier members.
    <p style="margin-top:20px">Please click <span class="red">here</span> to download the LFG Associate Membership application. Return a completed form to office@lakeshorefreightwaysguild.com or mail to our mailing address.</p>
    <p style="margin-top:58px"><span class="outline-btn">Meet our Members</span></p>
  </div>
</section>

<h2 class="abs section-title" style="top:3308px">Newsletter</h2>
<section>
  <div class="abs photo" style="top:3365px;height:425px;background:linear-gradient(90deg,#2a2a40 0%,#6a5a7a 40%,#b07a70 70%,#40304a 100%)" role="img" aria-label="Locomotive under a purple sunset sky"></div>
  <div class="abs panel" style="left:605px;top:3365px;width:420px;height:425px;background:var(--purple)">
    <p style="margin:18px 0 22px">Subscribe to our Newsletter and receive latest updates.</p>
    <div class="field">Name*</div>
    <div class="field">Email*</div>
    <p style="margin-top:14px"><span class="outline-btn">Subscribe</span></p>
  </div>
</section>

<h2 class="abs section-title" style="top:3830px">Contact Us</h2>
<footer>
  <div class="abs contact-band"></div>
  <div class="abs contact-buttons"><span>RESOURCES</span><span>RAILROADS &amp; VETERANS</span></div>
  <div class="abs contact-item" style="left:300px;top:3935px;width:200px">
    <svg width="18" height="24" viewBox="0 0 18 24"><path d="M9 1a7.5 7.5 0 0 0-7.5 7.5C1.5 14 9 23 9 23s7.5-9 7.5-14.5A7.5 7.5 0 0 0 9 1z" fill="none" stroke="#fff" stroke-width="1.6"/><circle cx="9" cy="8.5" r="2.6" fill="none" stroke="#fff" stroke-width="1.6"/></svg>
    410 Harbor Street,<br>Suite 200 Muskegon, MI 49440
  </div>
  <div class="abs contact-item" style="left:540px;top:3941px;width:110px">
    <svg width="20" height="20" viewBox="0 0 20 20"><path d="M4 2l3 1 1 4-2 1.5a10 10 0 0 0 5.5 5.5L13 12l4 1 1 3-2 2C9 18 2 11 2 4z" fill="none" stroke="#fff" stroke-width="1.5"/></svg>
    (555) 214-0187
  </div>
  <div class="abs contact-item" style="left:665px;top:3941px;width:110px">
    <svg width="22" height="20" viewBox="0 0 22 20"><rect x="5" y="1" width="12" height="6" fill="none" stroke="#fff" stroke-width="1.5"/><rect x="1" y="7" width="20" height="8" fill="none" stroke="#fff" stroke-width="1.5"/><rect x="5" y="12" width="12" height="7" fill="none" stroke="#fff" stroke-width="1.5"/></svg>
    (555) 214-0190
  </div>
  <div class="abs contact-item" style="left:790px;top:3941px;width:280px">
    <svg width="22" height="18" viewBox="0 0 22 18"><rect x="1" y="1" width="20" height="16" fill="none" stroke="#fff" stroke-width="1.5"/><polyline points="1,1 11,10 21,1" fill="none" stroke="#fff" stroke-width="1.5"/></svg>
    office@lakeshorefreightwaysguild.com
  </div>
  <div class="abs footbar">
    <span>© Copyright 2017. LFG. All rights reserved.</span>
    <div class="socials"><span></span><span></span><span></span><span></span><span></span></div>
  </div>
</footer>

</body>
</html>
```